A new website for Electrical Contractor Business

We are looking for a unique and new WordPress website design which would include 5 Pages - Home Page, Meet the Team, Our Services, Our Projects and Contact Us page.

The global theme for the website needs to be professional but simple to navigate as we cater for both business and home owner customers.

Our core business service is targeted around lighting from single room decorative to large office so the theme should incorporate this in some way.

The home page should include;
Our business logo, Contact number, Email address, small Image rotation box - Highlighting pervious projectsText box - With welcome message, chirpnet feed news reel/Customer feed back box.

I would also like to see a 2 boxes for the separate customer types we services. Business and Home Owner. each box will have a small image with a small text description with a link to the area of the services page relevant to that customer type.

Meet the team page -This will be introducing potential customers to the team so I would like it to include for each team member. Something like a small image and text area which will introduce an outline of the team members skills and abilities.

Our Services page This page will be outlining the different services on offer to the both customer types business and homeowner. Each service should have an image with text description of the service would good here.

Our projects page-Will include images of pervious projects and work we have completed along with a text area for the project description/ outliner.

Contact Us page - Should include a contact form which should include an option for the customer to quest us to call them back, also a selection box for them to inform us our how they found our details would be good.

Colour - The theme colours can be taken from the logo or feel free to impress with your own imagination.

Remember we are looking for a website that will interest our customers enough to except our services or be drawn further into the website.. So call to action links to other areas of the site/ contact page are welcome

Target Market(s)

Business - Office, warehousing and Large Store - lighting and Power
Home owner lighting and power

Coding

Coded - Design and coding required

Number of Pages Required

5+ page

Font styles to use
Serif
Sans Serif

Colors

Designer to choose colors to be used in the design.

Requirements
Must have
• Logo integrated into the website design - i.e. website colours which allow the logo to blend into the design.
Nice to have
• Custom but professional theme catering to business customers, but also show that we do provide services to home owners too.
Should not have
• Sorry am not interested in one oversized block image on rotation covering half the home page.. Images will be needed but not a single block over sized frame with not text, shape. Please use your imagination when considering this design

```html
<!DOCTYPE html>
<html lang="en">
<head>
<meta charset="utf-8">
<title>Voltline Electrical — Expert Electricians and Remodellers</title>
<link rel="stylesheet" href="https://fonts.googleapis.com/css2?family=Poppins:wght@300;400;500;600;700&family=Open+Sans:wght@400;600&display=swap">
<style>
:root{
  --navy:#1f3466;
  --orange:#f26a22;
  --coral:#f06a5a;
  --dark:#1e1f22;
  --ink:#2b2b2b;
  --grey:#6f6f6f;
  --light:#ececec;
  --footer:#2a2a2a;
  --footer-deep:#1d1d1d;
  --yellow:#f7c21a;
}
*{margin:0;padding:0;box-sizing:border-box}
html,body{width:1200px;height:4010px;overflow:hidden;background:#fff}
body{position:relative;font-family:"Open Sans",sans-serif;color:var(--ink)}
.abs{position:absolute}
.heading{font-family:"Poppins",sans-serif;font-weight:600}

/* top bar */
.topbar{left:0;top:0;width:1200px;height:44px;background:var(--navy);color:#fff;font-family:"Poppins",sans-serif;font-size:16px}
.topbar .item{position:absolute;top:0;height:44px;display:flex;align-items:center;gap:8px}
.book-now{position:absolute;left:871px;top:0;width:241px;height:44px;background:var(--coral);color:#fff;font-weight:600;font-size:15px;display:flex;align-items:center;justify-content:center;gap:6px}

/* header */
.header{left:0;top:44px;width:1200px;height:84px;background:#fff}
.brand{position:absolute;left:78px;top:10px;height:64px;display:flex;align-items:center;gap:10px;font-family:"Poppins",sans-serif;font-weight:500;font-size:19px;color:var(--navy)}
.brand .dot{width:22px;height:22px;border-radius:50%;background:var(--orange)}
.nav a{position:absolute;top:34px;font-family:"Poppins",sans-serif;font-size:15px;color:var(--navy);text-decoration:none}

/* hero */
.hero{left:0;top:128px;width:1200px;height:445px;background:linear-gradient(100deg,#3a3530 0%,#2a2826 45%,#1f1f20 100%)}
.hero-person{position:absolute;left:101px;top:30px;width:265px;height:415px;background:linear-gradient(180deg,#d9a24a,#b97a2c 60%,#e2c12a);border-radius:6px}
.hero h1{position:absolute;left:431px;top:136px;font-family:"Poppins",sans-serif;font-weight:600;font-size:26px;color:var(--orange);letter-spacing:.2px}
.hero p{position:absolute;left:431px;top:180px;width:670px;font-size:14.5px;line-height:26.5px;color:#e6e6e6}
.btn{position:absolute;top:332px;height:31px;display:flex;align-items:center;justify-content:center;font-family:"Poppins",sans-serif;font-size:14px;color:#fff}
.btn-solid{left:431px;width:123px;background:var(--orange)}
.btn-ghost{left:560px;width:123px;border:2px solid #d8d8d8}

/* audience band */
.audience{left:0;top:573px;width:1200px;height:114px;background:var(--orange);color:#fff}
.audience .seg{position:absolute;top:0;height:114px;display:flex;align-items:center;gap:22px;font-family:"Poppins",sans-serif;font-weight:400;font-size:50px}
.audience .divider{position:absolute;left:586px;top:14px;width:2px;height:86px;background:rgba(255,255,255,.6)}

/* section titles */
.title{font-family:"Poppins",sans-serif;font-weight:600;font-size:23px}
.bolt-rule{display:flex;align-items:center;gap:6px}
.bolt-rule span{display:block;width:64px;height:1px;background:currentColor;opacity:.6}

/* why choose us */
.why-photo{left:73px;top:741px;width:417px;height:292px;background:linear-gradient(135deg,#c9ccd0,#7b8794 50%,#35506e)}
.why-title{left:518px;top:733px;color:var(--ink)}
.why-rule{left:518px;top:765px;color:var(--orange)}
.why-rule span{width:64px}
.why-lead{left:518px;top:797px;width:560px;font-size:17.5px;line-height:27px;color:#3a3a3a}
.feature{position:absolute;width:275px;display:flex;gap:16px}
.feature .ico{flex:none;width:44px;height:44px;background:var(--orange);display:flex;align-items:center;justify-content:center}
.feature h3{font-family:"Poppins",sans-serif;font-weight:600;font-size:14.5px;color:#333;margin-bottom:2px}
.feature p{font-size:12.5px;line-height:15.5px;color:var(--grey)}

/* services */
.services{left:0;top:1118px;width:1200px;height:477px;background:linear-gradient(180deg,#1b2330,#26303d 55%,#1a2029)}
.services .title{position:absolute;left:0;width:1200px;top:40px;text-align:center;color:#fff}
.services .bolt-rule{position:absolute;left:0;width:1200px;top:72px;justify-content:center;color:#fff}
.svc{position:absolute;top:127px;width:237px;height:272px;border:2px solid var(--orange);display:flex;flex-direction:column;align-items:center;justify-content:center;gap:14px;color:#fff;font-family:"Poppins",sans-serif;font-size:22px;line-height:27px;text-align:center}
.svc.active{background:var(--orange)}

/* testimonials */
.testi-title{left:0;width:1200px;top:1632px;text-align:center;color:var(--ink)}
.testi-rule{left:0;width:1200px;top:1664px;justify-content:center;color:var(--orange)}
.quote{left:350px;top:1740px;width:494px;text-align:center;font-size:12.5px;line-height:20px;color:#555}
.qmark{top:1745px;font-family:Georgia,serif;font-size:110px;line-height:110px;color:#b9b9b9;font-weight:700}
.client{left:0;width:1200px;top:1824px;text-align:center}
.client b{display:block;font-family:"Poppins",sans-serif;font-weight:500;font-size:17px;color:var(--navy)}
.client span{font-size:15px;color:#444}
.arrow{top:1857px;width:34px;height:34px;border-radius:50%;border:1px solid #cfcfcf;display:flex;align-items:center;justify-content:center}
.avatar{left:550px;top:1898px;width:94px;height:94px;border-radius:50%;border:3px solid var(--yellow);background:radial-gradient(circle,#fbe3c4,#f6b77c)}
.dots{top:2018px;height:4px}
.to-top{left:1141px;top:1964px;width:36px;height:36px;border-radius:50%;background:var(--navy);display:flex;align-items:center;justify-content:center}

/* offers */
.offers{left:0;top:2073px;width:1200px;height:852px;background:var(--orange);color:#fff}
.offers .title{position:absolute;left:0;width:1200px;top:38px;text-align:center}
.offers .bolt-rule{position:absolute;left:0;width:1200px;top:70px;justify-content:center;color:#fff}
.vline{position:absolute;top:143px;width:1px;height:639px;background:rgba(255,255,255,.6)}
.hline{position:absolute;left:73px;width:1039px;height:1px;background:rgba(255,255,255,.6)}
.offer{position:absolute;width:340px;text-align:center;font-family:"Poppins",sans-serif}
.offer .small{font-size:15px;line-height:16px;font-weight:400;text-transform:uppercase}
.offer .big{font-size:56px;line-height:58px;font-weight:700}
.offer .sub{font-size:16px;font-weight:400;text-transform:uppercase;margin-top:2px}

/* location & comments */
.lower{left:0;top:2925px;width:1200px;height:455px;background:var(--light)}
.lower .title{position:absolute;top:54px;color:var(--ink)}
.lower .bolt-rule{position:absolute;top:86px;color:var(--orange)}
.map{left:163px;top:125px;width:327px;height:244px;background:linear-gradient(135deg,#e9eee3,#d6e2cc 55%,#e5e9ee)}
.video{left:600px;top:125px;width:408px;height:244px;background:linear-gradient(135deg,#6c5a4a,#b8a892 55%,#3d3a38);border:3px solid #222}
.video .cap{position:absolute;left:10px;top:10px;color:#fff;font-size:14px}

/* badges */
.badge{top:3429px;width:100px;height:100px;border-radius:50%;background:#8a8a8a;border:4px solid #cfcfcf}

/* footer */
.footer{left:0;top:3576px;width:1200px;height:384px;background:var(--footer);color:#ddd}
.footer h4{position:absolute;top:52px;font-family:"Poppins",sans-serif;font-weight:500;font-size:16px;color:#fff}
.contact-row{position:absolute;left:86px;display:flex;align-items:center;gap:18px;font-size:13.5px;line-height:17px}
.contact-row .ci{flex:none;width:40px;height:40px;border-radius:50%;background:#1f1f1f;display:flex;align-items:center;justify-content:center}
.links a{position:absolute;font-size:13px;color:#ddd;text-decoration:none;padding-left:18px}
.links a::before{content:"›";position:absolute;left:0;top:-3px;color:var(--orange);font-size:17px}
.promo{left:808px;top:54px;width:333px;height:195px;border:1px dashed #6d6d6d;text-align:center;font-family:"Poppins",sans-serif}
.promo .line{margin-top:30px;font-size:22px;color:#fff}
.promo .line b{font-size:50px;font-weight:700;color:var(--yellow);vertical-align:-6px;margin:0 4px}
.promo .what{font-size:16px;color:#fff;margin-top:2px}
.copyright{left:0;top:3960px;width:1200px;height:50px;background:var(--footer-deep);color:#aaa;font-size:11.5px;display:flex;align-items:center;justify-content:center}
</style>
</head>
<body>

<!-- top bar -->
<div class="abs topbar">
  <div class="item" style="left:472px">
    <svg width="20" height="15" viewBox="0 0 20 15"><rect x="1" y="1" width="18" height="13" rx="1.5" fill="none" stroke="#fff" stroke-width="2"/><path d="M1 2l9 7 9-7" fill="none" stroke="#fff" stroke-width="2"/></svg>
    hello@voltline.com
  </div>
  <div class="item" style="left:718px">
    <svg width="26" height="26" viewBox="0 0 26 26"><circle cx="12" cy="12" r="10" fill="none" stroke="#fff" stroke-width="1.6"/><path d="M12 6v6l4 3" fill="none" stroke="#fff" stroke-width="1.6"/></svg>
    0400 555 012
  </div>
  <div class="book-now">
    <svg width="14" height="14" viewBox="0 0 14 14"><circle cx="7" cy="7" r="6" fill="none" stroke="#fff" stroke-width="2"/><path d="M7 3.5v4l2.5 1.5" fill="none" stroke="#fff" stroke-width="1.6"/></svg>
    BOOK NOW
  </div>
</div>

<!-- header -->
<header class="abs header">
  <div class="brand"><span class="dot"></span>Voltline Electrical</div>
  <nav class="nav">
    <a href="#" style="left:510px">HOME</a>
    <a href="#" style="left:579px">MEET THE TEAM</a>
    <a href="#" style="left:720px">OUR SERVICES</a>
    <a href="#" style="left:854px">OUR PROJECTS</a>
    <a href="#" style="left:1000px">CONTACT US</a>
  </nav>
</header>

<!-- hero -->
<section class="abs hero">
  <div class="hero-person" role="img" aria-label="Smiling electrician in hard hat and overalls holding a yellow toolbox and cable"></div>
  <h1>EXPERT ELECTRICIANS AND REMODELLERS</h1>
  <p>Sed ut perspiciatis unde omnis iste natus error sit voluptatem accusantium doloremque laudantium, totam rem aperiam, eaque ipsa quae ab illo inventore veritatis et quasi architecto beatae vitae dicta sunt explicabo. Nemo enim ipsam voluptatem quia voluptas sit aspernatur aut odit aut fugit, sed quia consequuntur magni dolores eos qui ratione voluptatem sequi nesciunt</p>
  <a class="btn btn-solid">Learn More</a>
  <a class="btn btn-ghost">Get A Quote</a>
</section>

<!-- audience -->
<section class="abs audience">
  <div class="seg" style="left:190px">
    <svg width="50" height="56" viewBox="0 0 50 56" fill="none" stroke="#fff" stroke-width="2"><circle cx="25" cy="20" r="16"/><circle cx="25" cy="20" r="9"/><path d="M15 33l-7 18 8-3 4 7 5-12M35 33l7 18-8-3-4 7-5-12"/></svg>
    Business
  </div>
  <div class="divider"></div>
  <div class="seg" style="left:660px">
    <svg width="50" height="58" viewBox="0 0 50 58" fill="none" stroke="#fff" stroke-width="2"><path d="M12 14a10 9 0 0 1 20 0z"/><circle cx="22" cy="21" r="7"/><path d="M8 56V42a14 12 0 0 1 28 0v14M30 46h14v10H30z"/></svg>
    Home Owner
  </div>
</section>

<!-- why choose us -->
<div class="abs why-photo" role="img" aria-label="Hand working on a switchboard full of circuit breakers and coloured wiring"></div>
<h2 class="abs title why-title">Why Choose Us</h2>
<div class="abs bolt-rule why-rule"><svg width="10" height="18" viewBox="0 0 10 18"><path d="M6 0L0 10h4l-2 8 8-11H6l2-7z" fill="currentColor"/></svg></div>
<p class="abs why-lead">It is a long established fact that a reader will be distracted by the readable content of a page when looking at its layout.</p>

<div class="feature" style="left:518px;top:881px">
  <div class="ico"><svg width="18" height="24" viewBox="0 0 18 24" fill="none" stroke="#fff" stroke-width="2"><path d="M9 2a7 7 0 0 0-4 12.7V18h8v-3.3A7 7 0 0 0 9 2zM6 21h6"/></svg></div>
  <div><h3>Safety First</h3><p>We never compromise on the safety of our customers</p></div>
</div>
<div class="feature" style="left:826px;top:881px">
  <div class="ico"><svg width="18" height="24" viewBox="0 0 18 24" fill="none" stroke="#fff" stroke-width="2"><path d="M9 2a7 7 0 0 0-4 12.7V18h8v-3.3A7 7 0 0 0 9 2zM6 21h6"/></svg></div>
  <div><h3>Up Front Affordable Pricing</h3><p>We tailor a solution to your needs and agree on a price before work begins.</p></div>
</div>
<div class="feature" style="left:518px;top:969px">
  <div class="ico"><svg width="18" height="24" viewBox="0 0 18 24" fill="none" stroke="#fff" stroke-width="2"><path d="M9 2a7 7 0 0 0-4 12.7V18h8v-3.3A7 7 0 0 0 9 2zM6 21h6"/></svg></div>
  <div><h3>Professional Work</h3><p>Clean, tidy, respectful tradesmen who take all their rubbish away at the end of the job.</p></div>
</div>
<div class="feature" style="left:826px;top:969px">
  <div class="ico"><svg width="18" height="24" viewBox="0 0 18 24" fill="none" stroke="#fff" stroke-width="2"><path d="M9 2a7 7 0 0 0-4 12.7V18h8v-3.3A7 7 0 0 0 9 2zM6 21h6"/></svg></div>
  <div><h3>Excellence Guarantee</h3><p>You will always receive polite and friendly customer service.</p></div>
</div>

<!-- services -->
<section class="abs services" role="img" aria-label="Row of spanners hanging on a dark tool wall">
  <h2 class="title">Our &nbsp;Services</h2>
  <div class="bolt-rule"><span></span><svg width="10" height="18" viewBox="0 0 10 18"><path d="M6 0L0 10h4l-2 8 8-11H6l2-7z" fill="currentColor"/></svg><span></span></div>
  <div class="svc active" style="left:73px">
    <svg width="56" height="60" viewBox="0 0 56 60" fill="none" stroke="#fff" stroke-width="2"><path d="M28 14a13 13 0 0 0-7 24v6h14v-6a13 13 0 0 0-7-24zM22 48h12M24 52h8M28 2v6M8 10l4 4M48 10l-4 4M2 28h6M48 28h6"/></svg>
    Lighting
  </div>
  <div class="svc" style="left:341px">
    <svg width="56" height="60" viewBox="0 0 56 60" fill="none" stroke="#fff" stroke-width="2"><circle cx="24" cy="20" r="8"/><path d="M14 15h20M8 56V44a16 12 0 0 1 32 0v12M14 48h20v8H14zM40 6l10 10-4 4-10-10z"/></svg>
    Commercial<br>Electrician
  </div>
  <div class="svc" style="left:605px">
    <svg width="48" height="60" viewBox="0 0 48 60" fill="none" stroke="#fff" stroke-width="2"><rect x="4" y="4" width="40" height="52"/><rect x="12" y="12" width="24" height="36"/><rect x="19" y="20" width="10" height="20"/></svg>
    Switchboard<br>installation
  </div>
  <div class="svc" style="left:874px">
    <svg width="56" height="60" viewBox="0 0 56 60" fill="none" stroke="#fff" stroke-width="2"><path d="M14 20a14 12 0 0 1 28 0zM10 20h36"/><circle cx="28" cy="28" r="8"/><path d="M8 58V48a20 12 0 0 1 40 0v10z"/></svg>
    Emergency<br>Electrician
  </div>
</section>

<!-- testimonials -->
<h2 class="abs title testi-title">Testimonials</h2>
<div class="abs bolt-rule testi-rule"><span></span><svg width="10" height="18" viewBox="0 0 10 18"><path d="M6 0L0 10h4l-2 8 8-11H6l2-7z" fill="currentColor"/></svg><span></span></div>
<div class="abs qmark" style="left:262px">“</div>
<p class="abs quote">Lorem Ipsum is simply dummy text of the printing and typesetting industry. Lorem Ipsum has been the industry's standard dummy text ever since the 1500s, when an unknown printer took a galley of type and scrambled it to make a type specimen book.</p>
<div class="abs qmark" style="left:878px">”</div>
<div class="abs client"><b>Client Name</b><span>Designation</span></div>
<div class="abs arrow" style="left:131px"><svg width="10" height="14" viewBox="0 0 10 14"><path d="M7 2L2 7l5 5" fill="none" stroke="#aaa" stroke-width="1.6"/></svg></div>
<div class="abs arrow" style="left:1028px"><svg width="10" height="14" viewBox="0 0 10 14"><path d="M3 2l5 5-5 5" fill="none" stroke="#aaa" stroke-width="1.6"/></svg></div>
<svg class="abs" style="left:585px;top:1880px" width="24" height="16" viewBox="0 0 24 16"><path d="M12 0L24 16H0z" fill="var(--yellow)"/></svg>
<div class="abs avatar" role="img" aria-label="Client portrait"></div>
<div class="abs dots" style="left:489px;width:70px;background:var(--yellow)"></div>
<div class="abs dots" style="left:563px;width:70px;background:var(--navy)"></div>
<div class="abs dots" style="left:637px;width:69px;background:var(--navy)"></div>
<div class="abs to-top"><svg width="14" height="10" viewBox="0 0 14 10"><path d="M2 8l5-5 5 5" fill="none" stroke="#fff" stroke-width="2"/></svg></div>

<!-- offers -->
<section class="abs offers">
  <h2 class="title">Our Existing Offers</h2>
  <div class="bolt-rule"><span></span><svg width="10" height="18" viewBox="0 0 10 18"><path d="M6 0L0 10h4l-2 8 8-11H6l2-7z" fill="currentColor"/></svg><span></span></div>
  <div class="vline" style="left:430px"></div>
  <div class="vline" style="left:781px"></div>
  <div class="hline" style="top:336px"></div>
  <div class="hline" style="top:544px"></div>

  <div class="offer" style="left:82px;top:190px"><div class="big">$50 OFF</div><div class="sub">When you book online</div></div>
  <div class="offer" style="left:436px;top:178px"><div class="small">We are open</div><div class="big">24 HRS</div><div class="sub" style="margin-top:12px">For your service</div></div>
  <div class="offer" style="left:777px;top:196px"><div class="big">$ % OFF</div><div class="sub">For senior citizen</div></div>

  <div class="offer" style="left:82px;top:392px"><div class="small">Hot offer</div><div class="big">$ 45</div><div class="sub" style="margin-top:10px">Home electrical inspection</div></div>
  <div class="offer" style="left:436px;top:392px"><div class="small">Ceiling fan at</div><div class="big">$269</div><div class="sub" style="margin-top:10px">(Inclusive supply and fitting)</div></div>
  <div class="offer" style="left:777px;top:392px"><div class="small">LED oyster lights for</div><div class="big">$89</div><div class="sub" style="margin-top:10px">(Inclusive supply and fitting)</div></div>

  <div class="offer" style="left:82px;top:613px"><div class="small">Air conditioner for</div><div class="big">$1050</div><div class="sub" style="margin-top:10px">(Inclusive supply and fitting)</div></div>
  <div class="offer" style="left:444px;top:620px"><div class="big">$50 OFF</div><div class="sub">When you book online</div></div>
  <div class="offer" style="left:800px;top:610px"><div class="small">We are open</div><div class="big">24 HRS</div><div class="sub" style="margin-top:12px">For your service</div></div>
</section>

<!-- location & comments -->
<section class="abs lower">
  <h2 class="title" style="left:163px">Our Location</h2>
  <div class="bolt-rule" style="left:163px"><span></span><svg width="10" height="18" viewBox="0 0 10 18"><path d="M6 0L0 10h4l-2 8 8-11H6l2-7z" fill="var(--orange)"/></svg><span></span></div>
  <h2 class="title" style="left:600px">Comments of Clients</h2>
  <div class="bolt-rule" style="left:600px"><span></span><svg width="10" height="18" viewBox="0 0 10 18"><path d="M6 0L0 10h4l-2 8 8-11H6l2-7z" fill="var(--orange)"/></svg><span></span></div>
  <div class="abs map" role="img" aria-label="Street map of the service area"></div>
  <div class="abs video" role="img" aria-label="Video of a client speaking in her kitchen"><span class="cap">ClientVoice Testimonial</span></div>
</section>

<!-- badges -->
<div class="abs badge" style="left:163px"></div>
<div class="abs badge" style="left:431px"></div>
<div class="abs badge" style="left:695px"></div>
<div class="abs badge" style="left:963px"></div>

<!-- footer -->
<footer class="abs footer">
  <h4 style="left:86px">CONTACT US</h4>
  <div class="contact-row" style="top:103px">
    <div class="ci"><svg width="12" height="18" viewBox="0 0 12 18"><rect x="1" y="1" width="10" height="16" rx="2" fill="none" stroke="var(--orange)" stroke-width="2"/></svg></div>
    <div><span style="font-size:15px;color:#fff">+1 555 010 4477</span><br><span style="font-size:12px">Support 24/7 Weekdays</span></div>
  </div>
  <div class="contact-row" style="top:157px">
    <div class="ci"><svg width="14" height="18" viewBox="0 0 14 18"><path d="M7 17s6-6 6-10A6 6 0 0 0 1 7c0 4 6 10 6 10z" fill="var(--orange)"/><circle cx="7" cy="7" r="2" fill="#1f1f1f"/></svg></div>
    <div>Harbor Point, 12 Lumen Street, NY 10001</div>
  </div>
  <div class="contact-row" style="top:210px">
    <div class="ci"><svg width="16" height="12" viewBox="0 0 16 12"><rect x="1" y="1" width="14" height="10" fill="none" stroke="var(--orange)" stroke-width="1.6"/><path d="M1 1l7 6 7-6" fill="none" stroke="var(--orange)" stroke-width="1.6"/></svg></div>
    <div>info@voltline.com</div>
  </div>
  <div class="contact-row" style="top:264px">
    <div class="ci"><svg width="16" height="16" viewBox="0 0 16 16"><circle cx="8" cy="8" r="7" fill="none" stroke="var(--orange)" stroke-width="1.6"/><path d="M8 4v4l3 2" fill="none" stroke="var(--orange)" stroke-width="1.6"/></svg></div>
    <div>Weekdays: 09:00am - 06:00pm</div>
  </div>

  <h4 style="left:447px">OUR SERVICES</h4>
  <div class="links">
    <a style="left:447px;top:101px">Electrical</a>
    <a style="left:447px;top:134px">Plumbing</a>
    <a style="left:447px;top:168px">Engine Repair</a>
    <a style="left:447px;top:201px">Repair House</a>
    <a style="left:447px;top:234px">Home Maintenance</a>
    <a style="left:447px;top:267px">Wall Paint</a>
    <a style="left:626px;top:101px">Installation</a>
    <a style="left:626px;top:134px">Garden Repairs</a>
    <a style="left:626px;top:168px">Soil Drilling</a>
    <a style="left:626px;top:201px">Support 24/7</a>
    <a style="left:626px;top:234px">Inspection House</a>
    <a style="left:626px;top:267px">Remodeling Ceiling</a>
  </div>

  <div class="abs promo">
    <div class="line">GET<b>25%</b>OFF</div>
    <div class="what">Electrical Services</div>
  </div>
</footer>
<div class="abs copyright">Copyright @ 2019. All rights reserved</div>

</body>
</html>
```